Paint Protection Options

This is a flyer that will describe two different paint protection options for vehicles. I have mocked up a Word doc. As well, I've included some samples of other flyers where I like the "look". I am not locked into any single layout or design. In my Word doc I have them side-by-side. I think that makes sense but open to ideas. I've also added some pics of the two options being applied to cars. We need to have one of each (ceramic and ppf) at a minimum. In the grid I'm thinking different colors dots/circles to differentiate the different levels. But again, I'm open to suggestions. You can use the symbol for microns in the grid under the Thickness row. I spelled it out because I didn't know how to insert.

```html
<!DOCTYPE html>
<html lang="en">
<head>
<meta charset="utf-8">
<title>Paint Protection Options</title>
<link href="https://fonts.googleapis.com/css2?family=Poppins:wght@400;500;600;700;800&display=swap" rel="stylesheet">
<style>
:root{
  --backdrop:#444444;
  --paper:#f4f4f4;
  --ink:#2a2a2a;
  --text:#4a4a4a;
  --green:#4cb848;
  --green-dark:#17703a;
  --blue:#3a6cc4;
  --blue-light:#4f86d9;
  --pink:#e91e63;
  --pink-dark:#d81b4f;
  --yellow:#f2c12e;
  --red:#e0332d;
  --line:#c8c8c8;
}
*{box-sizing:border-box;margin:0;padding:0}
html,body{width:1200px;height:1200px;overflow:hidden;background:var(--backdrop);font-family:'Poppins',sans-serif}
.flyer{position:absolute;left:175px;top:0;width:850px;height:1200px;background:linear-gradient(160deg,#fafafa 0%,#eeeeee 50%,#f8f8f8 100%);}
.title-bar{position:absolute;left:48px;top:49px;width:759px;height:71px;border-radius:22px 22px 0 0;background:linear-gradient(90deg,var(--green) 0%,#3aa543 60%,var(--green-dark) 100%);display:flex;align-items:center;justify-content:center;}
.title-bar::after{content:"";position:absolute;left:367px;bottom:-8px;border-left:9px solid transparent;border-right:9px solid transparent;border-top:8px solid #2f9a41}
.title-bar h1{color:#fff;font-weight:800;font-size:43px;letter-spacing:-1px;padding-left:24px}
.photo{position:absolute;top:136px;height:141px}
.photo-ceramic{left:48px;width:373px;background:linear-gradient(120deg,#1b2d8a 0%,#2b47b8 40%,#e07a3a 55%,#1c2a6e 100%)}
.photo-film{left:425px;width:383px;background:linear-gradient(110deg,#b8121f 0%,#d8283a 40%,#c9ccd2 65%,#2a2a2e 100%)}
.panel{position:absolute;top:281px;left:48px;width:760px;height:449px;background:#f1f1f1;border-radius:0 0 12px 12px;border:1px solid #ddd}
.side-label{position:absolute;top:0;width:45px;height:449px;background:var(--ink);display:flex;align-items:center;justify-content:center}
.side-label span{writing-mode:vertical-rl;transform:rotate(180deg);color:#fff;font-weight:700;font-size:27px;letter-spacing:-.5px;white-space:nowrap}
.side-left{left:0;border-radius:0 0 0 12px}
.side-right{right:0;border-radius:0 0 12px 0}
.divider{position:absolute;left:376px;top:0;height:449px;border-left:1px dashed #888}
.copy{position:absolute;top:4px;color:var(--text);font-size:14px;line-height:17px}
.copy p{margin-bottom:17px}
.copy-ceramic{left:69px;width:290px}
.copy-film{left:399px;width:292px}
.benefits{list-style:none;margin-top:-6px}
.benefits li{position:relative;padding-left:24px;color:var(--ink);font-weight:600;font-size:14px;line-height:17px;margin-bottom:4px}
.copy-film .benefits li{margin-bottom:9px}
.benefits svg{position:absolute;left:0;top:1px}
.table{position:absolute;left:49px;top:761px;width:769px}
.table-head{display:grid;grid-template-columns:242px 175px 176px 176px;height:49px;align-items:end}
.head-feature{background:var(--ink);color:#fff;font-weight:700;font-size:21px;height:34px;padding-left:32px;line-height:34px}
.head-col{height:49px;border-radius:8px 8px 0 0;color:#fff;font-weight:600;font-size:14.5px;padding:16px 0 0 22px}
.col-wax{background:linear-gradient(160deg,var(--blue-light),#2f5fb5)}
.col-ceramic{background:linear-gradient(160deg,#f03c6a,var(--pink-dark))}
.col-film{background:linear-gradient(160deg,#57c24f,#35a33c)}
.table-body{background:#fff;padding-top:4px}
.row{display:grid;grid-template-columns:242px 175px 176px 176px;height:27.7px;align-items:center}
.row .feature{display:flex;align-items:center;gap:6px;padding-left:15px;color:#333;font-size:15px}
.row .cell{display:flex;align-items:center;gap:8px;padding-left:12px;color:#444;font-size:13px;height:100%;background:#f7f7f7}
.row.boxed .cell{border:1px solid var(--line);border-left:none;border-right:none;background:#fff}
.row.boxed .cell:last-child{border-right:1px solid var(--line)}
.row.boxed .cell:nth-child(2){border-left:1px solid var(--line)}
.dot{width:11px;height:11px;border-radius:50%;flex:none;position:relative}
.dot::after{content:"";position:absolute;left:3px;top:2px;width:3px;height:5px;border:solid #fff;border-width:0 1.5px 1.5px 0;transform:rotate(45deg)}
.d-blue{background:var(--blue)}
.d-green{background:var(--green)}
.d-red{background:var(--red)}
.d-yellow{background:conic-gradient(var(--green) 0 50%,var(--yellow) 50% 100%)}
.d-quarter{background:conic-gradient(var(--green) 0 25%,var(--yellow) 25% 100%)}
.d-three{background:conic-gradient(var(--blue) 0 75%,var(--green) 75% 100%)}
.icon{width:18px;height:18px;flex:none}
.table-foot{display:grid;grid-template-columns:242px 175px 176px 176px;height:32px}
.table-foot div{color:#fff;font-weight:600;font-size:14px;padding:4px 0 0 32px}
.table-foot .foot-label{background:var(--ink);padding:6px 0 0 21px;font-size:15px}
.table-foot .foot-wax{background:linear-gradient(160deg,var(--blue-light),#2f5fb5)}
.table-foot .foot-ceramic{background:var(--pink-dark)}
.table-foot .foot-film{background:linear-gradient(90deg,#35a33c,#58c24c)}
</style>
</head>
<body>
<main class="flyer">
  <header class="title-bar"><h1>PAINT PROTECTION OPTIONS</h1></header>

  <div class="photo photo-ceramic" role="img" aria-label="Photo of an orange microfibre cloth buffing ceramic coating on a blue car"></div>
  <div class="photo photo-film" role="img" aria-label="Photo of clear paint protection film being applied to a red car"></div>

  <section class="panel">
    <div class="side-label side-left"><span>CERAMIC COATINGS</span></div>
    <div class="divider"></div>
    <div class="copy copy-ceramic">
      <p>Ceramic coatings are liquid polymer coatings that bond to a vehicle’s painted surface. The coatings are formulated to retain the showroom finish by protecting against corrosion and contaminants like UV damage, oxidation, road salt and acid rain. Ceramic coatings give your car a deep, glossy finish that reflects light and makes your paint look more vibrant while greatly extending the paint's lifespan.</p>
      <p>The chemical bonding process improves color depth and leaves a smooth finish. The hydrophobic (water repellent) properties repel water and dirt as well as protect against damaging pollutants. This makes care and maintenance a breeze while retaining the show room finish. Never wax again!</p>
      <ul class="benefits">
        <li><svg width="17" height="17" viewBox="0 0 17 17"><path d="M8.5 1 16 8.5 8.5 16 1 8.5Z" fill="none" stroke="#4cb848" stroke-width="1.4"/><path d="M5.5 8.7 7.7 10.8 11.5 6.5" fill="none" stroke="#4cb848" stroke-width="1.4"/></svg>Enhance and retain showroom finish</li>
        <li><svg width="17" height="17" viewBox="0 0 17 17"><path d="M8.5 1 16 8.5 8.5 16 1 8.5Z" fill="none" stroke="#4cb848" stroke-width="1.4"/><path d="M5.5 8.7 7.7 10.8 11.5 6.5" fill="none" stroke="#4cb848" stroke-width="1.4"/></svg>Protect against corrosion and contaminants</li>
        <li><svg width="17" height="17" viewBox="0 0 17 17"><path d="M8.5 1 16 8.5 8.5 16 1 8.5Z" fill="none" stroke="#4cb848" stroke-width="1.4"/><path d="M5.5 8.7 7.7 10.8 11.5 6.5" fill="none" stroke="#4cb848" stroke-width="1.4"/></svg>Reduce care and maintenance</li>
      </ul>
    </div>
    <div class="copy copy-film">
      <p>Paint Protection Film (PPF) is a transparent, thermoplastic urethane film that is applied directly to the car’s painted surfaces. PPF excels at shielding your vehicle from rock chips, scratches, and other physical damage. It has self-healing properties that can repair minor scratches and swirl marks over time.</p>
      <p>Every piece of PPF is custom cut to fit each panel of your vehicle and provide maximum coverage. The film protects your vehicle from scratches, rock chips, staining, corrosion, fading, chemicals, insects, and road debris. It helps keep your paint looking new, saving you money and improving your resale value.</p>
      <ul class="benefits">
        <li><svg width="17" height="17" viewBox="0 0 17 17"><path d="M8.5 1 16 8.5 8.5 16 1 8.5Z" fill="none" stroke="#4cb848" stroke-width="1.4"/><path d="M5.5 8.7 7.7 10.8 11.5 6.5" fill="none" stroke="#4cb848" stroke-width="1.4"/></svg>Protect against rock chips, scratches, and physical damage</li>
        <li><svg width="17" height="17" viewBox="0 0 17 17"><path d="M8.5 1 16 8.5 8.5 16 1 8.5Z" fill="none" stroke="#4cb848" stroke-width="1.4"/><path d="M5.5 8.7 7.7 10.8 11.5 6.5" fill="none" stroke="#4cb848" stroke-width="1.4"/></svg>Easily repair minor scratches and swirl marks</li>
        <li><svg width="17" height="17" viewBox="0 0 17 17"><path d="M8.5 1 16 8.5 8.5 16 1 8.5Z" fill="none" stroke="#4cb848" stroke-width="1.4"/><path d="M5.5 8.7 7.7 10.8 11.5 6.5" fill="none" stroke="#4cb848" stroke-width="1.4"/></svg>Protect against corrosion and contaminants</li>
      </ul>
    </div>
    <div class="side-label side-right"><span>PAINT PROTECTION FILM (PPF)</span></div>
  </section>

  <section class="table">
    <div class="table-head">
      <div class="head-feature">FEATURE</div>
      <div class="head-col col-wax">Car Wax</div>
      <div class="head-col col-ceramic">Ceramic Coating</div>
      <div class="head-col col-film">Paint Protection Film</div>
    </div>
    <div class="table-body">
      <div class="row">
        <div class="feature"><svg class="icon" viewBox="0 0 18 18" fill="none" stroke="#3a8fd9" stroke-width="1.2"><path d="M4 2h10M4 16h10M5 2c0 5 8 5 8 7s-8 2-8 7M13 2c0 5-8 5-8 7s8 2 8 7"/></svg>Duration</div>
        <div class="cell"><span class="dot d-blue"></span>2 - 4 Weeks</div>
        <div class="cell"><span class="dot d-blue"></span>3 - 10 Years</div>
        <div class="cell"><span class="dot d-blue"></span>7 - 10 Years</div>
      </div>
      <div class="row boxed">
        <div class="feature"><svg class="icon" viewBox="0 0 18 18" fill="none" stroke="#3a8fd9" stroke-width="1.2"><path d="M9 1v16M11 1v16M2 9h5M13 9h4M5 7l2 2-2 2M15 7l-2 2 2 2"/></svg>Thickness</div>
        <div class="cell"><span class="dot d-blue"></span>.5 - 1.5 µm</div>
        <div class="cell"><span class="dot d-blue"></span>7 - 10 µm</div>
        <div class="cell"><span class="dot d-blue"></span>200 - 250 µm</div>
      </div>
      <div class="row">
        <div class="feature"><svg class="icon" viewBox="0 0 18 18" fill="none" stroke="#3a8fd9" stroke-width="1.2"><path d="M7 2l1.5 4.5L13 8l-4.5 1.5L7 14l-1.5-4.5L1 8l4.5-1.5zM14 10l.8 2.2 2.2.8-2.2.8L14 16l-.8-2.2L11 13l2.2-.8z"/></svg>Gloss Enhancement</div>
        <div class="cell"><span class="dot d-green"></span>Full Circle - green</div>
        <div class="cell"><span class="dot d-green"></span>Full Circle - green</div>
        <div class="cell"><span class="dot d-green"></span>Full Circle - green</div>
      </div>
      <div class="row boxed">
        <div class="feature"><svg class="icon" viewBox="0 0 18 18" fill="none" stroke="#3a8fd9" stroke-width="1.2"><path d="M4 11a3 3 0 0 1 0-6 4 4 0 0 1 8-1 3.5 3.5 0 0 1 1 7zM6 13l-1 3M9 13l-1 3M12 13l-1 3"/></svg>Acid Rain Damage</div>
        <div class="cell"><span class="dot d-yellow"></span>1/2 Circle - Yellow</div>
        <div class="cell"><span class="dot d-green"></span>Full Circle - green</div>
        <div class="cell"><span class="dot d-green"></span>Full Circle - green</div>
      </div>
      <div class="row">
        <div class="feature"><svg class="icon" viewBox="0 0 18 18" fill="none" stroke="#3a8fd9" stroke-width="1.2"><path d="M9 2l8 14H1zM9 7v4M9 13v1"/></svg>Corrosion Prevention</div>
        <div class="cell"><span class="dot d-yellow"></span>1/2 Circle - Yellow</div>
        <div class="cell"><span class="dot d-green"></span>Full Circle - green</div>
        <div class="cell"><span class="dot d-green"></span>Full Circle - green</div>
      </div>
      <div class="row boxed">
        <div class="feature"><svg class="icon" viewBox="0 0 18 18" fill="none" stroke="#3a8fd9" stroke-width="1.2"><path d="M1 12c3-2 5 2 8 0s5 2 8 0M1 15c3-2 5 2 8 0s5 2 8 0M5 7a4 4 0 0 1 8 0M9 1v2M3 4l1 1M15 4l-1 1"/></svg>UV/Oxidation Protection</div>
        <div class="cell"><span class="dot d-yellow"></span>1/2 Circle - Yellow</div>
        <div class="cell"><span class="dot d-green"></span>Full Circle - green</div>
        <div class="cell"><span class="dot d-green"></span>Full Circle - green</div>
      </div>
      <div class="row">
        <div class="feature"><svg class="icon" viewBox="0 0 18 18" fill="none" stroke="#3a8fd9" stroke-width="1.2"><path d="M9 3c3 4 5 7 5 9a5 5 0 0 1-10 0c0-2 2-5 5-9zM5 1l1 2"/></svg>Hard Water Damage</div>
        <div class="cell"><span class="dot d-quarter"></span>1/4 Circle - Yellow</div>
        <div class="cell"><span class="dot d-three"></span>3/4 Circle - green</div>
        <div class="cell"><span class="dot d-green"></span>Full Circle - green</div>
      </div>
      <div class="row boxed">
        <div class="feature"><svg class="icon" viewBox="0 0 18 18" fill="none" stroke="#3a8fd9" stroke-width="1.2"><ellipse cx="9" cy="10" rx="3.5" ry="5.5"/><circle cx="9" cy="3.5" r="1.5"/><path d="M5.5 8H2M5.5 11H2M5.5 14l-3 2M12.5 8H16M12.5 11H16M12.5 14l3 2M9 5v10"/></svg>Insect Splatter Damage</div>
        <div class="cell"><span class="dot d-quarter"></span>1/4 Circle - Yellow</div>
        <div class="cell"><span class="dot d-three"></span>3/4 Circle - green</div>
        <div class="cell"><span class="dot d-green"></span>Full Circle - green</div>
      </div>
      <div class="row">
        <div class="feature"><svg class="icon" viewBox="0 0 18 18" fill="none" stroke="#3a8fd9" stroke-width="1.2"><path d="M9 1l6 2v5c0 4-3 7-6 8-3-1-6-4-6-8V3zM6 8l2 2 4-4"/></svg>Chip Protection</div>
        <div class="cell"><span class="dot d-red"></span>Full Circle -red</div>
        <div class="cell"><span class="dot d-quarter"></span>1/4 Circle - Yellow</div>
        <div class="cell"><span class="dot d-green"></span>Full Circle - green</div>
      </div>
      <div class="row boxed">
        <div class="feature"><svg class="icon" viewBox="0 0 18 18" fill="none" stroke="#3a8fd9" stroke-width="1.2"><path d="M2 14h14l-1-6-4-4H6L2 8zM5 9l3-3M8 10l3-3"/></svg>Scratch Protection</div>
        <div class="cell"><span class="dot d-red"></span>Full Circle -red</div>
        <div class="cell"><span class="dot d-quarter"></span>1/4 Circle - Yellow</div>
        <div class="cell"><span class="dot d-green"></span>Full Circle - green</div>
      </div>
      <div class="row">
        <div class="feature"><svg class="icon" viewBox="0 0 18 18" fill="none" stroke="#3a8fd9" stroke-width="1.2"><path d="M1 12h16v-2l-3-1-2-3H6L4 9l-3 1zM4 12a1.5 1.5 0 0 0 3 0M11 12a1.5 1.5 0 0 0 3 0"/></svg>Swirl Protection</div>
        <div class="cell"><span class="dot d-red"></span>Full Circle -red</div>
        <div class="cell"><span class="dot d-red"></span>Full Circle -red</div>
        <div class="cell"><span class="dot d-green"></span>Full Circle - green</div>
      </div>
    </div>
    <div class="table-foot">
      <div class="foot-label">Application Complexity</div>
      <div class="foot-wax">Low</div>
      <div class="foot-ceramic">Medium</div>
      <div class="foot-film">High</div>
    </div>
  </section>
</main>
</body>
</html>
```